Business Card for IT company

I need a high tech looking business card using our logo. I prefer something clean and modern.

Target Market(s)

Buyers of IT hardware and software, IT Techies who are key influencers

Industry/Entity Type

Business

```html
<!DOCTYPE html>
<html lang="en">
<head>
<meta charset="utf-8">
<title>Novaridge Consulting – Business Card</title>
<link rel="stylesheet" href="https://fonts.googleapis.com/css2?family=Montserrat:wght@400;600&family=Oswald:wght@500;600&family=Arimo:wght@400&display=swap">
<style>
  :root{
    --stage:#e6e7e8;
    --frame:#2a2a2a;
    --paper:#fbfbfb;
    --ink:#2c2c2c;
    --green-dark:#3a9e3f;
    --green-light:#a2d150;
    --green-pale:#b6dc6e;
    --bar-grey:#d7d7d7;
    --tint:#ececec;
  }
  html,body{margin:0;padding:0;overflow:hidden;}
  body{width:1200px;height:743px;background:var(--stage);position:relative;font-family:"Arimo",Arial,sans-serif;}
  .card{position:absolute;top:221px;width:520px;height:300px;box-sizing:border-box;border:10px solid var(--frame);background:var(--paper);overflow:hidden;box-shadow:0 10px 24px rgba(0,0,0,.18);}
  .card--front{left:60px;}
  .card--back{left:620px;}

  /* front */
  .brand{position:absolute;font-family:"Montserrat",sans-serif;font-weight:600;color:var(--ink);line-height:1;}
  .brand__name{font-size:34px;letter-spacing:-.5px;}
  .brand__sub{font-size:11px;letter-spacing:7px;margin-top:6px;}
  .brand__mark{display:inline-block;width:12px;height:12px;background:var(--green-dark);margin-left:8px;vertical-align:middle;}
  .card--front .brand{left:38px;top:62px;}

  .name-bar{position:absolute;left:230px;right:0;top:100px;height:45px;background:linear-gradient(90deg,var(--bar-grey),#f2f2f2);display:flex;align-items:center;padding-left:14px;gap:10px;}
  .name{font-family:"Oswald",sans-serif;font-weight:600;font-size:22px;color:var(--ink);}
  .name__first{color:var(--green-dark);}
  .role{font-size:12px;color:var(--ink);}
  .role::before{content:"/ ";font-size:18px;}

  .green-field{position:absolute;left:0;right:0;top:145px;bottom:0;background:linear-gradient(180deg,var(--green-pale),var(--green-light));}
  .url-band{position:absolute;left:0;width:230px;top:145px;height:50px;background:var(--green-dark);display:flex;align-items:center;justify-content:center;}
  .url-band span{font-family:"Montserrat",sans-serif;font-weight:600;font-size:14px;color:#fff;letter-spacing:.5px;}

  .contact{position:absolute;left:250px;top:155px;margin:0;padding:0;list-style:none;font-size:12px;line-height:16px;color:var(--ink);}

  /* back */
  .pattern-field{position:absolute;inset:0;background:linear-gradient(160deg,var(--tint),var(--paper) 75%);}
  .card--back .brand{right:30px;bottom:46px;text-align:left;}
  .card--back .brand__name{font-size:40px;}
  .card--back .brand__sub{font-size:12px;letter-spacing:9px;}
  .back-url{position:absolute;right:30px;bottom:22px;font-family:"Montserrat",sans-serif;font-weight:600;font-size:17px;color:var(--green-dark);letter-spacing:1px;}
</style>
</head>
<body>
  <section class="card card--front" aria-label="Card front">
    <div class="green-field"></div>
    <div class="brand">
      <div class="brand__name">Novaridge<span class="brand__mark"></span></div>
      <div class="brand__sub">CONSULTING</div>
    </div>
    <div class="name-bar">
      <span class="name"><span class="name__first">Alan</span>Brooks</span>
      <span class="role">Programmer</span>
    </div>
    <div class="url-band"><span>www.novaridge.com</span></div>
    <ul class="contact">
      <li>IT Company</li>
      <li>P : 404-555-0182</li>
      <li>F : 404-555-0183</li>
      <li>email : alan@novaridge.com</li>
      <li>twitter : @alanbrooks</li>
    </ul>
  </section>

  <section class="card card--back" aria-label="Card back">
    <div class="pattern-field" role="img" aria-label="Faint repeated brand lettering pattern in light grey"></div>
    <div class="brand">
      <div class="brand__name">Novaridge<span class="brand__mark"></span></div>
      <div class="brand__sub">CONSULTING</div>
    </div>
    <div class="back-url">www.novaridge.com</div>
  </section>
</body>
</html>
```